create a webpage for optometry practice

I'm looking to create a professional and elegant webpage for my practice. I prefer neutral earthy colors, but I am open to other ideas. I have included an image of my logo to be used in the process. This will be a page that will illustrate information about my practice and the kind of services we offer. I am in process of having the practice remodeled. So I don't have any photos of my practice to include yet.

Target Market(s)

My practice serves young and mature families.

Font styles to use
Sans Serif

Colors
33a6d7
86cfc6
85cae6
cadf82
3276b5
faa54b
abd036
f78c1e

Requirements
Must have
• I would need to incorporate information about my practice, services, insurance accepted, make appointment, contact us, and about our family.
Nice to have
• I would like to see something fresh, modern, and unique

```html
<!DOCTYPE html>
<html lang="en">
<head>
<meta charset="utf-8">
<title>Clearview Eye Care</title>
<link rel="stylesheet" href="https://fonts.googleapis.com/css2?family=Josefin+Sans:wght@400;600;700&family=Open+Sans:wght@400;600&display=swap">
<style>
:root{
  --teal:#1a9ca2;
  --teal-dark:#14868b;
  --charcoal:#3b3b3d;
  --charcoal-deep:#2e2e30;
  --orange:#e8842b;
  --orange-deep:#d06d14;
  --brown:#7b5a3b;
  --brown-dark:#5e4229;
  --ink:#333;
  --muted:#777;
  --line:#d9d9d9;
  --paper:#ffffff;
  --mist:#f3f3f3;
}
*{box-sizing:border-box;margin:0;padding:0}
html,body{width:1200px;height:3843px;overflow:hidden}
body{font-family:"Open Sans",sans-serif;color:var(--ink);background:var(--paper);font-size:15px;line-height:1.55}
.heading{font-family:"Josefin Sans",sans-serif;font-variant:small-caps;letter-spacing:1px}

/* top bar */
.topbar{height:48px;background:var(--teal);display:flex;align-items:center;justify-content:space-between;padding:0 70px;color:#fff;font-size:14px}
.social{display:flex;gap:10px}
.social span{width:22px;height:22px;background:rgba(255,255,255,.85);border-radius:3px}
.topbar .meta{display:flex;gap:28px;align-items:center}
.topbar .meta b{font-weight:600}

/* header */
.header{height:124px;display:flex;align-items:center;justify-content:space-between;padding:0 70px}
.brand{display:flex;align-items:center;gap:12px}
.brand .dot{width:34px;height:34px;border-radius:50%;background:var(--teal)}
.brand .name{font-family:"Josefin Sans",sans-serif;font-size:34px;font-weight:600;color:var(--charcoal);letter-spacing:1px}
.btn-book{background:var(--teal);color:#fff;font-family:"Josefin Sans",sans-serif;font-size:20px;padding:12px 26px;letter-spacing:1px}

/* nav */
.nav{margin:0 70px;height:56px;background:linear-gradient(var(--brown),var(--brown-dark));display:flex;align-items:center;padding-left:10px;position:relative}
.nav a{font-family:"Josefin Sans",sans-serif;font-variant:small-caps;color:#fff;text-decoration:none;font-size:22px;padding:0 16px;height:56px;display:flex;align-items:center;border-right:1px solid rgba(255,255,255,.35)}
.nav a.active{background:var(--orange)}
.nav .search{margin-left:auto;margin-right:14px;width:330px;height:34px;background:#fff;display:flex;align-items:center;justify-content:space-between;padding:0 12px;font-size:14px;color:#999}

/* hero */
.hero{margin:24px 0 0;height:328px;position:relative;background:linear-gradient(90deg,#8c8c8c,#cfcfcf 45%,#9a9a9a);}
.hero .photo{position:absolute;inset:0}
.hero .badge{position:absolute;left:640px;top:64px;width:440px;height:200px;background:rgba(255,255,255,.92);display:flex;align-items:center}
.hero .diamond{position:absolute;left:-60px;top:40px;width:120px;height:120px;background:var(--teal);transform:rotate(45deg);border:6px solid #fff}
.hero .num{position:absolute;left:-60px;top:40px;width:120px;height:120px;display:flex;align-items:center;justify-content:center;color:#fff;font-family:"Josefin Sans",sans-serif;font-size:56px;font-weight:700}
.hero .copy{margin-left:100px;font-family:"Josefin Sans",sans-serif;font-variant:small-caps;color:var(--charcoal);line-height:1.1}
.hero .copy .big{font-size:54px;color:var(--teal-dark)}
.hero .copy .sub{font-size:34px}

/* appointment */
.appointment{height:660px;padding-top:20px;position:relative}
.appointment .title{text-align:center;font-size:40px;color:var(--charcoal);line-height:1.1}
.appointment .title small{display:block;font-size:28px;color:var(--muted)}
.form{position:absolute;left:80px;top:140px;width:460px;height:460px;border:1px solid var(--line);padding:22px 24px;font-size:11px}
.form label{display:block;font-weight:600;text-transform:uppercase;color:#555;font-size:11px;margin-bottom:4px}
.form .field{height:30px;border:1px solid var(--line);margin-bottom:14px;padding:6px 8px;color:#aaa}
.form .row{display:flex;gap:16px}.form .row>div{flex:1}
.form .area{height:64px}
.form .times{display:flex;gap:14px;margin-bottom:18px}
.form .times span{flex:1;height:30px;border:1px solid var(--line);display:flex;align-items:center;justify-content:center;text-transform:uppercase;color:#666}
.form .foot{display:flex;justify-content:space-between;align-items:center}
.form .foot i{display:inline-block;width:11px;height:11px;border:1px solid #999;margin-right:6px;vertical-align:middle}
.form .send{background:var(--teal);color:#fff;padding:8px 26px;text-transform:uppercase}
.doctor{position:absolute;left:600px;top:130px;width:500px;height:480px;background:radial-gradient(circle at 50% 35%,#f2e6da,#e3ecef 60%,#fff 90%)}

/* info split */
.split{height:488px;display:flex}
.split > div{flex:1;padding:40px 70px;color:#fff}
.story{background:var(--charcoal)}
.services{background:var(--teal)}
.split .heading{text-align:center;line-height:1.1;margin-bottom:24px}
.split .heading small{display:block;font-size:20px}
.split .heading span{font-size:32px}
.split p{font-size:14px;margin-bottom:16px;line-height:1.5}
.list{display:grid;grid-template-columns:1fr 1fr;gap:4px 24px;font-size:14px;margin-top:20px}
.list li{list-style:none}
.list li::before{content:"";display:inline-block;width:9px;height:9px;background:#fff;border-radius:50%;margin-right:8px}
.more{display:inline-block;margin-top:30px;border:2px solid rgba(255,255,255,.7);padding:4px 22px;font-size:13px;text-transform:uppercase}
.story .more{background:var(--teal)}
.services .more{background:var(--charcoal)}

/* gallery */
.gallery{height:600px;padding-top:48px}
.tabs{display:flex;justify-content:center;gap:10px;margin-bottom:30px}
.tabs span{padding:4px 16px;color:#fff;background:var(--teal);font-size:15px}
.tabs span.all{background:var(--charcoal)}
.grid{display:grid;grid-template-columns:repeat(4,250px);gap:26px 20px;justify-content:center}
.grid div{height:210px}
.g1{background:linear-gradient(135deg,#c9a98a,#8d6f57)}
.g2{background:linear-gradient(135deg,#e0dcd6,#a8a49e)}
.g3{background:linear-gradient(135deg,#d9e3e8,#a7b8c1)}
.g4{background:linear-gradient(135deg,#d7b28c,#a27a52)}
.g5{background:linear-gradient(135deg,#b9c3c9,#6f7c86)}
.g6{background:linear-gradient(135deg,#c7d3cf,#87989a)}
.g7{background:linear-gradient(135deg,#c9b39c,#7d6756)}
.g8{background:linear-gradient(135deg,#e3c9a9,#b38b62)}

/* testimonials */
.testimonials{height:400px;background:var(--charcoal-deep);color:#fff;text-align:center;padding-top:36px;position:relative}
.testimonials .quote{font-size:60px;line-height:.6;font-family:Georgia,serif}
.testimonials .heading{font-size:28px;line-height:1.1;margin-top:20px}
.testimonials p{font-family:"Josefin Sans",sans-serif;font-variant:small-caps;width:900px;margin:16px auto 0;font-size:19px;line-height:1.3}
.testimonials .avatar{width:70px;height:70px;border-radius:50%;background:linear-gradient(#b99a7f,#7b604c);margin:26px auto 8px;border:3px solid #fff}
.testimonials .who{font-size:13px;font-variant:small-caps}
.arrow{position:absolute;top:176px;width:26px;height:40px}
.arrow.l{left:90px}.arrow.r{right:90px}

/* insurance & contact */
.bottom{height:620px;display:flex}
.insurance{flex:1;background:var(--teal);color:#fff;padding:50px 80px}
.contact{flex:1;background:var(--orange);color:#fff;padding:50px 80px}
.bottom .heading{font-size:30px;text-align:center;margin-bottom:20px;padding-bottom:12px;border-bottom:1px solid rgba(255,255,255,.5)}
.insurance p{font-size:14px;margin-bottom:18px}
.insurance .plans{text-align:center;font-size:14px;margin-bottom:18px}
.insurance .plans span{display:block;text-decoration:underline}
.contact label{display:block;font-size:17px;margin-bottom:4px}
.contact .field{height:40px;border:3px solid var(--charcoal);background:var(--orange-deep);margin-bottom:14px}
.contact .area{height:110px}
.contact .send{display:block;width:110px;margin:16px auto 0;text-align:center;background:var(--orange-deep);border:2px solid #fff;padding:4px 0;text-transform:uppercase;font-size:15px}

/* footer */
.footer{height:380px;background:var(--charcoal);color:#ccc;display:grid;grid-template-columns:1.1fr 1.1fr 1fr 1fr;gap:40px;padding:40px 70px;font-size:13px}
.footer h4{font-family:"Josefin Sans",sans-serif;font-variant:small-caps;color:#fff;font-size:19px;font-weight:400;margin-bottom:14px;letter-spacing:1px}
.links{display:grid;grid-template-columns:1fr 1fr;gap:8px;text-transform:uppercase;font-size:12px}
.newsletter .box{display:flex;margin-top:14px}
.newsletter .box span{flex:1;height:34px;background:#fff;color:#999;padding:8px;font-size:12px}
.newsletter .box b{width:40px;background:var(--teal)}
.hours div{display:flex;justify-content:space-between;padding:8px 0;border-bottom:1px solid #555}
.contact-info p{margin-bottom:10px}
.copyright{height:83px;background:var(--charcoal-deep);color:#ccc;display:flex;align-items:center;justify-content:center;font-family:"Josefin Sans",sans-serif;font-variant:small-caps;font-size:16px;letter-spacing:1px}
</style>
</head>
<body>

<div class="topbar">
  <div class="social"><span></span><span></span><span></span><span></span><span></span><span></span></div>
  <div class="meta"><span><b>Emergency call:</b> +1 555 014 2290</span><span>Login</span><span>|</span><span>Register</span></div>
</div>

<header class="header">
  <div class="brand"><span class="dot"></span><span class="name">CLEARVIEW EYE CARE</span></div>
  <div class="btn-book">BOOK APPOINTMENT</div>
</header>

<nav class="nav">
  <a class="active">Home</a><a>About Us</a><a>Services</a><a>My Practice</a><a>Contact Us</a>
  <div class="search"><span>Search</span>
    <svg width="16" height="16" viewBox="0 0 16 16"><circle cx="6.5" cy="6.5" r="5" fill="none" stroke="#555" stroke-width="2"/><line x1="10" y1="10" x2="15" y2="15" stroke="#555" stroke-width="2"/></svg>
  </div>
</nav>

<section class="hero">
  <div class="photo" role="img" aria-label="Optometrist examining a patient's eyes with clinic equipment, in grey tones"></div>
  <div class="badge">
    <div class="diamond"></div><div class="num">10</div>
    <div class="copy"><div class="big">Years of</div><div class="sub">Dedicated</div><div class="sub">Quality Services</div></div>
  </div>
</section>

<section class="appointment">
  <h2 class="title heading">Book an Appointment<small>It's easy and fast</small></h2>
  <div class="form">
    <label>First name &amp; last name</label><div class="field">Enter your name</div>
    <label>Contact number</label><div class="field">Enter your phone</div>
    <div class="row"><div><label>Date from</label><div class="field">Select date</div></div><div><label>Date to</label><div class="field">Select date</div></div></div>
    <label>Message</label><div class="field area">Type your message</div>
    <label>Select preferred time</label>
    <div class="times"><span>Morning</span><span>Lunch</span><span>Evening</span></div>
    <div class="foot"><span><i></i>Add me to mailing list</span><span class="send">Send request</span></div>
  </div>
  <div class="doctor" role="img" aria-label="Smiling optometrist in a white coat with a stethoscope, gesturing toward the form"></div>
</section>

<section class="split">
  <div class="story">
    <h3 class="heading"><small>Our Story</small><span>About EYE Care</span></h3>
    <p>Lorem Ipsum has been the industry's standard dummy text ever since the 1500s, when an unknown printer took a galley of type and scrambled it to make a type specimen book. It has survived not only five centuries, but also the leap into electronic typesetting, remaining essentially unchanged.</p>
    <p>Lorem Ipsum is simply dummy text of the printing and typesetting industry. Lorem Ipsum has been the industry's standard dummy text ever since the 1500s, when an unknown printer took a galley of type and scrambled it to make a type specimen book.</p>
    <span class="more">Read more</span>
  </div>
  <div class="services">
    <h3 class="heading"><small>Services of Clearview</small><span>Our Services</span></h3>
    <p>Lorem Ipsum is simply dummy text of the printing and typesetting industry. Lorem Ipsum has been the industry's standard dummy text ever since the 1500s, when an unknown printer took a galley of type and scrambled it to make a type specimen book.</p>
    <ul class="list">
      <li>Comprehensive eye exams</li><li>Pediatric vision checks</li>
      <li>Contact lens fitting</li><li>Glaucoma screening</li>
      <li>Dry eye treatment</li><li>Designer eyewear</li>
      <li>Diabetic eye care</li><li>Low vision support</li>
      <li>Sports vision care</li><li>Emergency eye visits</li>
    </ul>
    <span class="more">Read more</span>
  </div>
</section>

<section class="gallery">
  <div class="tabs"><span class="all">All</span><span>Doctor</span><span>Doctor 1</span><span>Doctor 2</span></div>
  <div class="grid">
    <div class="g1" role="img" aria-label="Patient at a slit lamp during an eye exam"></div>
    <div class="g2" role="img" aria-label="Optometrist checking a patient's vision"></div>
    <div class="g3" role="img" aria-label="Doctor using an eye examination instrument"></div>
    <div class="g4" role="img" aria-label="Optometrist consulting with a patient at a desk"></div>
    <div class="g5" role="img" aria-label="Patient looking into a phoropter"></div>
    <div class="g6" role="img" aria-label="Eye pressure test in the clinic"></div>
    <div class="g7" role="img" aria-label="Doctor examining a young patient"></div>
    <div class="g8" role="img" aria-label="Vision screening with a patient seated"></div>
  </div>
</section>

<section class="testimonials">
  <div class="quote">&ldquo;</div>
  <h3 class="heading">What our patients have to say<br>We are reliable &amp; trusted</h3>
  <p>Lorem Ipsum is simply dummy text of the printing and typesetting industry. Lorem Ipsum has been the industry's standard dummy text ever since the 1500s, when an unknown printer took a galley of type and scrambled it to make a type specimen book.</p>
  <div class="avatar" role="img" aria-label="Patient portrait"></div>
  <div class="who">Dana Morel, Parent</div>
  <svg class="arrow l" viewBox="0 0 26 40"><polyline points="20,4 6,20 20,36" fill="none" stroke="#fff" stroke-width="4"/></svg>
  <svg class="arrow r" viewBox="0 0 26 40"><polyline points="6,4 20,20 6,36" fill="none" stroke="#fff" stroke-width="4"/></svg>
</section>

<section class="bottom">
  <div class="insurance">
    <h3 class="heading">Accepted Health Insurance</h3>
    <p>Lorem Ipsum has been the industry's standard dummy text ever since the 1500s, when an unknown printer took a galley of type and scrambled it to make a type specimen book. It has survived not only five centuries, but also the leap into electronic typesetting, remaining essentially unchanged.</p>
    <div class="plans"><span>All Health Insurance Plans and Networks</span><span>Health Exchange Marketplace (Affordable Care Act)</span><span>Medicare Government and Private Providers</span></div>
    <p>Lorem Ipsum is simply dummy text of the printing and typesetting industry. Lorem Ipsum has been the industry's standard dummy text ever since the 1500s, when an unknown printer took a galley of type and scrambled it to make a type specimen book.</p>
  </div>
  <div class="contact">
    <h3 class="heading">Get In Touch</h3>
    <label>Your Name</label><div class="field"></div>
    <label>Your E-Mail</label><div class="field"></div>
    <label>Subject</label><div class="field"></div>
    <label>Your Message</label><div class="field area"></div>
    <span class="send">Send</span>
  </div>
</section>

<footer class="footer">
  <div><h4>Quick Links</h4>
    <div class="links"><span>Doctors</span><span>Terms of use</span><span>Services</span><span>Privacy policy</span><span>Gallery</span><span>Disclaimer</span><span>FAQs</span><span>Sitemap</span></div>
  </div>
  <div class="newsletter"><h4>Signup for Newsletter</h4>
    <p>Get eye health tips, clinic news and seasonal offers sent to your inbox each month.</p>
    <div class="box"><span>Enter your e-mail</span><b></b></div>
  </div>
  <div class="hours"><h4>Opening Hours</h4>
    <div><span>Monday - Friday</span><span>9:00am - 6:00pm</span></div>
    <div><span>Saturday</span><span>9:00am - 2:00pm</span></div>
    <div><span>Sunday</span><span>Closed</span></div>
  </div>
  <div class="contact-info"><h4>Contact Us</h4>
    <p>48 Birchwood Lane<br>Millbrook, ON 00000</p>
    <p>Phone: +1 555 014 2290</p>
    <p>Email: hello@clearvieweye.example</p>
  </div>
</footer>
<div class="copyright">Copyright &copy; 2015 Clearview Eye Care, All Right Reserved</div>

</body>
</html>
```